Premium Personal Brand — Facebook Banner (Used Across All Platforms)

Update — Additional Color Direction
In addition to the dark charcoal/slate direction already described, I'm also interested in seeing variants with:
Dark navy blue — Deep, authoritative, intelligence-community feel. Same textured/matte treatment, not flat or bright.
Warm charcoal with steel blue accent — Keep the dark base but introduce a subtle steel blue gradient, accent line, or tonal shift. Sophisticated, modern, adds dimension without adding color noise.
Both should maintain the same premium, restrained, architectural feel described in the original brief. No bright blues, no corporate PowerPoint energy — think midnight, think depth, think weight.
Everything else in the brief remains the same.
I am building a premium personal brand as an executive advisor to founders ($5M+ revenue).
This contest is Facebook-banner–focused, but the design must represent a visual system that will be reused across:
- LinkedIn
- YouTube
I- nstagram
- X (Twitter)
- Website hero sections and other brand touchpoints
Think of the Facebook banner as the primary expression of the brand — not a one-off graphic.
This project is about discovering a high-end visual style and brand feel, not decoration.
What to design
Please submit one cohesive visual system, shown primarily as:
- Facebook banner (primary focus)
The same design language should clearly translate to all platforms listed above.
Designers are responsible for using the current recommended dimensions for each platform.
Quick clarification on background direction:
Backgrounds should have depth and texture, not flat color fields. Avoid pure white, light grey, or solid black backgrounds. Think matte, architectural materials — stone, graphite, concrete, steel — not blank canvases. Subtle tonal variation is encouraged. Obvious gradients or decorative patterns are not.
Text to use
Primary Headline:
- Your Business Is Too Valuable To Be Run On Hope.
Subheadline:
- You didn’t build a business to become its prisoner.
Name:
Paul Whitaker
The headline should be the dominant visual element.
Logo note (important)
My personal logo is currently being finalized.
For this contest:
- Use a simple “PW” monogram placeholder
- Clean, bold, geometric sans-serif
- Do not design a logo
- The winning design must allow an easy logo swap later.
Headshot note (important)
- Please do not include a headshot in the banner design.
- Most platforms display a circular profile image separately.
- The banner should stand on its own using typography, layout, and tone only.
- Design the banner assuming the profile photo will sit nearby, not inside the banner.
Style direction
The design should feel:
- Premium
- Calm
- Confident
- Restrained
- High-trust
- Dark, neutral backgrounds are preferred.
- Fewer elements are better than more.
Think:
- Owner-level advisor
- Private equity / boardroom tone
- Industrial, Modern, Minimalist, Elite, Architectural, not decorative
What to avoid
Please do not submit designs that feel:
- Promotional, hype-driven, or salesy
- Like a coach, guru, or agency
- Bright, colorful, or gradient-heavy
- Busy or over-designed
- Based on stock photos
- No motivational speaker energy.
Reaction test
- If someone sees this banner on Facebook (or later on LinkedIn, YouTube, etc.), the reaction should be:
“That person is serious. I’d trust them with important decisions.”
Final note
- I am not looking for many variations.
- I am looking for one strong visual direction you believe in.
Simple beats clever.
- Restraint beats decoration.

```html
<!DOCTYPE html>
<html lang="en">
<head>
<meta charset="UTF-8">
<title>Paul Whitaker — Banner</title>
<link rel="stylesheet" href="https://fonts.googleapis.com/css2?family=Montserrat:wght@300;400;700&display=swap">
<style>
  :root {
    --page: #ffffff;
    --graphite-deep: #050505;
    --graphite-mid: #161616;
    --graphite-light: #262626;
    --ink-light: #ffffff;
    --ink-soft: #f1f1f1;
  }
  html, body {
    margin: 0;
    padding: 0;
    width: 1200px;
    height: 700px;
    overflow: hidden;
    background: var(--page);
  }
  .canvas {
    position: relative;
    width: 1200px;
    height: 700px;
    background: var(--page);
  }
  .banner {
    position: absolute;
    left: 70px;
    top: 120px;
    width: 1060px;
    height: 465px;
    overflow: hidden;
    font-family: "Montserrat", sans-serif;
    color: var(--ink-light);
  }
  .banner-texture {
    position: absolute;
    inset: 0;
    background:
      radial-gradient(ellipse 45% 60% at 88% 45%, rgba(0,0,0,0.9), transparent 70%),
      radial-gradient(ellipse 40% 50% at 10% 80%, rgba(70,70,70,0.45), transparent 70%),
      radial-gradient(ellipse 35% 35% at 78% 10%, rgba(80,80,80,0.4), transparent 70%),
      radial-gradient(ellipse 60% 60% at 50% 55%, var(--graphite-light), transparent 80%),
      linear-gradient(180deg, var(--graphite-mid), var(--graphite-deep));
  }
  .headline {
    position: absolute;
    left: 0;
    right: 0;
    top: 192px;
    margin: 0;
    text-align: center;
    font-weight: 700;
    font-size: 28px;
    letter-spacing: 0.01em;
    line-height: 1.3;
  }
  .subheadline {
    position: absolute;
    left: 0;
    right: 0;
    top: 250px;
    margin: 0;
    text-align: center;
    font-weight: 400;
    font-size: 17px;
    letter-spacing: 0.09em;
    color: var(--ink-soft);
    line-height: 1.3;
  }
  .signature {
    position: absolute;
    left: 0;
    right: 0;
    top: 388px;
    display: flex;
    justify-content: center;
    align-items: baseline;
    gap: 13px;
  }
  .monogram {
    font-weight: 700;
    font-size: 24px;
    letter-spacing: -0.01em;
  }
  .name {
    font-weight: 300;
    font-size: 17px;
    letter-spacing: 0.02em;
    color: var(--ink-soft);
  }
</style>
</head>
<body>
  <main class="canvas">
    <section class="banner">
      <div class="banner-texture" role="img" aria-label="Dark textured graphite surface with fine speckled highlights"></div>
      <h1 class="headline">Your Business Is Too Valuable To Be Run On Hope.</h1>
      <p class="subheadline">You didn’t build a business to become its prisoner.</p>
      <div class="signature">
        <span class="monogram">PW</span>
        <span class="name">Paul Whitaker</span>
      </div>
    </section>
  </main>
</body>
</html>
```